BRAVEN CONSTRUCTION & RENOVATIONS
BRAVEN Construction & Renovations
Creative Brief
Professional
Marcus Wendell
Owner
482 Pallock Ln New Braunfels TX
Mwendell@bravenhomefix.com
www.bravenhomefix.com
Exterior and Interior FREE Estimates $0 down 5 star rated

```html
<!DOCTYPE html>
<html lang="en">
<head>
<meta charset="utf-8">
<title>Braven Construction &amp; Renovations – Business Cards</title>
<link rel="stylesheet" href="https://fonts.googleapis.com/css2?family=Tinos:ital,wght@0,400;0,700;1,400;1,700&display=swap">
<style>
  :root {
    --page-bg: #e6e2dc;
    --card-bg: #0b0b0b;
    --card-bg-edge: #191919;
    --brand-green: #3fd23a;
    --logo-silver: #c9ccd1;
    --ghost-grey: #242424;
    --text-white: #f2f2f2;
    --text-grey: #9a9a9a;
    --rule-grey: #4a4a4a;
    --tab-grey: #8a8a8a;
  }
  * { margin: 0; padding: 0; box-sizing: border-box; }
  html, body { width: 1200px; height: 713px; overflow: hidden; }
  body {
    background: var(--page-bg);
    font-family: "Tinos", "Times New Roman", serif;
    position: relative;
  }
  .card {
    position: absolute;
    top: 211px;
    width: 466px;
    height: 281px;
    border-radius: 16px;
    background: radial-gradient(ellipse at 50% 40%, var(--card-bg-edge), var(--card-bg) 70%);
    overflow: hidden;
    box-shadow: 0 4px 14px rgba(0,0,0,.25);
  }
  .card--front { left: 63px; }
  .card--back { left: 644px; }

  .ghost-name {
    position: absolute;
    left: 0; right: 0; top: 6px;
    text-align: center;
    font-weight: 700;
    font-size: 96px;
    letter-spacing: 4px;
    color: var(--ghost-grey);
    line-height: 1;
  }
  .brand {
    position: absolute;
    width: 250px;
    text-align: center;
  }
  .brand__name {
    font-weight: 700;
    font-size: 58px;
    line-height: 1;
    color: var(--logo-silver);
    letter-spacing: 1px;
  }
  .brand__tagline {
    margin-top: 8px;
    font-size: 10.5px;
    letter-spacing: 1.6px;
    color: var(--brand-green);
    text-transform: uppercase;
  }
  .brand__phone {
    margin-top: 14px;
    font-size: 20px;
    letter-spacing: 6px;
    color: var(--text-white);
  }
  .brand__web {
    margin-top: 16px;
    font-size: 8px;
    letter-spacing: 1.5px;
    color: var(--text-grey);
  }
  .card--front .brand { left: 0; top: 86px; }
  .card--back .brand { left: 108px; top: 86px; }

  .offer {
    position: absolute;
    left: 270px; top: 100px;
    width: 160px;
    text-align: center;
    font-size: 15px;
    line-height: 21px;
    color: var(--text-white);
  }
  .offer__highlight { color: var(--brand-green); font-style: italic; font-weight: 700; }

  .owner-tab {
    position: absolute;
    left: 5px; top: 12px;
    width: 9px; height: 34px;
    background: var(--tab-grey);
  }
  .owner {
    position: absolute;
    left: 20px; top: 11px;
  }
  .owner__name { font-size: 18px; font-weight: 700; color: var(--brand-green); line-height: 1.1; }
  .owner__role { font-size: 9px; color: var(--text-grey); }

  .rule {
    position: absolute;
    left: 89px; top: 206px;
    width: 336px; height: 1px;
    background: var(--rule-grey);
  }
  .contact {
    position: absolute;
    left: 116px; top: 215px;
    list-style: none;
    font-size: 10px;
    color: var(--text-white);
  }
  .contact li { display: flex; align-items: center; height: 19px; }
  .contact svg { width: 10px; height: 10px; margin-right: 5px; fill: var(--brand-green); }
</style>
</head>
<body>

<section class="card card--front" aria-label="Card front">
  <div class="ghost-name" aria-hidden="true">BRAVEN</div>
  <div class="brand">
    <div class="brand__name">BRAVEN</div>
    <div class="brand__tagline">Construction and Renovations</div>
    <div class="brand__phone">830.555.0148</div>
    <div class="brand__web">www.bravenhomefix.com</div>
  </div>
  <p class="offer">
    Exterior and Interior<br>
    <span class="offer__highlight">FREE Estimates</span><br>
    $0 down 5 star rated
  </p>
</section>

<section class="card card--back" aria-label="Card back">
  <div class="owner-tab"></div>
  <div class="owner">
    <div class="owner__name">Marcus Wendell</div>
    <div class="owner__role">Owner</div>
  </div>
  <div class="brand">
    <div class="brand__name">BRAVEN</div>
    <div class="brand__tagline">Construction and Renovations</div>
    <div class="brand__phone">830.555.0148</div>
  </div>
  <div class="rule"></div>
  <ul class="contact">
    <li>
      <svg viewBox="0 0 10 10" aria-hidden="true"><path d="M5 0a3.4 3.4 0 0 0-3.4 3.4C1.6 6 5 10 5 10s3.4-4 3.4-6.6A3.4 3.4 0 0 0 5 0zm0 4.8a1.4 1.4 0 1 1 0-2.8 1.4 1.4 0 0 1 0 2.8z"/></svg>
      482 Pallock Ln, New Braunfels TX
    </li>
    <li>
      <svg viewBox="0 0 10 10" aria-hidden="true"><path d="M0 2h10v6H0z M0 2l5 3.5L10 2" stroke="#0b0b0b" stroke-width=".8"/></svg>
      Mwendell@bravenhomefix.com
    </li>
    <li>
      <svg viewBox="0 0 10 10" aria-hidden="true"><circle cx="5" cy="5" r="5"/><path d="M0 5h10M5 0c-2 2.5-2 7.5 0 10M5 0c2 2.5 2 7.5 0 10" stroke="#0b0b0b" stroke-width=".7" fill="none"/></svg>
      www.bravenhomefix.com
    </li>
  </ul>
</section>

</body>
</html>
```